Modern, Clean website for painting service.

We are working with a company called Brush Harbor and building a new website for them.

Some sites to use for content/competitors and inspiration:

https://www.coatwellcrew.example
https://ridgeline-coats.example
https://tevinhallorpainting.example

Thank you for taking the time to consider designing a website for us. We are web developers based in Stockton, CA, USA. Most of our projects go through the same process. Understanding this process may help you win a project with us. We custom-code all of our websites in-house. We don’t have any requirements as to what tools you use for your design, but we prefer Figma files. For any design that we label as four-stars, we send it to the client for review. The client picks the final design they want us to use. Once we complete this process, we will continue to show additional clients all the four-star sites and purchase them later. Your designs will have multiple chances to sell. For better chances of success, we ask that you follow these guidelines.

IMAGES:
If you use any images or icons in the design, we ask that you have a link to the asset so we can purchase the image/icon. Most of the designs we submit do not have the customer’s images on them unless they have some great images. Be creative; show us the feeling you are trying to portray with your image choices. Use any royalty-free site you choose. We subscribe to Adobe and mainly use their images, but we can purchase images outside of Adobe. PLEASE NOTE: we will not submit designs to clients with watermarks on the images.

FONTS:
We ask that you identify the fonts used in the design. This can be done in a message if you want. We typically use Google Fonts and Adobe Fonts.

CONTENT:
We're always open to different content and ideas. We often submit designs with stock images so the client can see our vision. We typically take pictures after the website launch to use their images with our vision. Lorem Ipsum is fine for paragraphs, but we ask that you write the headers in correct English. We want to be able to show the vision and identify the sections of the website.

INSPIRATION:
We typically add a couple of links in the brief of websites we like to help you get started in your design.

REVISIONS:
We do not often ask for revisions of the designs unless we see something in the design that may not appeal to the client. If there are slight changes that we want to make, we do that in the development process.

FEEDBACK:
We rarely give feedback on designs during the design process. We are working on many website projects and do not have the time to provide feedback. We usually respond if your request is well thought out and asks specific questions, but a note asking “feedback, please” usually goes unanswered.

```html
<!DOCTYPE html>
<html lang="en">
<head>
<meta charset="utf-8">
<title>Brush Harbor – Elk Grove Painters</title>
<link href="https://fonts.googleapis.com/css2?family=Arimo:wght@400;700&display=swap" rel="stylesheet">
<style>
:root{
  --navy:#0b1f45;
  --red:#e3162b;
  --white:#ffffff;
  --mist:#e6e5ea;
  --ink:#222222;
  --night:#121212;
}
*{box-sizing:border-box;margin:0;padding:0}
html,body{width:1200px;height:5195px;overflow:hidden}
body{position:relative;font-family:"Arimo",Arial,sans-serif;color:var(--ink);background:var(--white)}
.abs{position:absolute}
.btn{position:absolute;display:flex;align-items:center;justify-content:center;font-size:18px;text-transform:uppercase}
.btn-red{background:var(--red);color:var(--white)}
.btn-line-white{border:2px solid var(--white);color:var(--white)}
.btn-line-red{border:2px solid var(--red);color:var(--red);background:var(--white)}
.photo{position:absolute}
.rule{position:absolute;height:3px;background:var(--red)}

/* header */
.brand{left:44px;top:16px;display:flex;align-items:center;gap:12px}
.brand-mark{width:26px;height:26px;border-radius:50%;background:var(--red)}
.brand-name{font-size:22px;font-weight:700;color:var(--navy);letter-spacing:2px}
.nav a{position:absolute;font-size:15px;color:var(--ink);text-decoration:none}
.nav .home{left:565px;top:50px;width:98px;height:36px;background:var(--red);color:var(--white);display:flex;align-items:center;justify-content:center}
.nav .cta{left:942px;top:46px;width:218px;height:42px;background:var(--navy);color:var(--white);display:flex;align-items:center;justify-content:center;font-size:15px}

/* hero */
.hero{left:0;top:126px;width:1200px;height:658px;background:var(--navy)}
.hero-title{left:48px;top:210px;color:var(--white);font-size:52px;font-weight:700;line-height:64px}
.hero-sub{left:48px;top:352px;color:var(--red);font-size:19px;font-weight:700}

/* services */
.section-title{position:absolute;left:0;width:1200px;text-align:center;font-size:30px}
.card{position:absolute;top:970px;width:362px;height:486px;padding:12px}
.card-navy{background:var(--navy)}
.card-red{background:var(--red)}
.card .photo{position:static;width:338px;height:220px}
.card h3{color:var(--white);font-weight:400;font-size:25px;text-align:center;margin-top:28px}
.card p{color:#d9dce4;font-size:14px;line-height:15px;text-align:center;margin:28px 20px 0}
.card .more{position:absolute;left:78px;top:406px;width:206px;height:56px;font-size:19px;text-transform:none}
.more-red{background:var(--red);color:var(--white)}
.more-line{border:1px solid var(--white);color:var(--white)}

/* about */
.about-bg{left:0;top:1680px;width:1200px;height:760px;background:var(--mist)}
.framed{border:8px solid var(--white)}
.kicker{left:670px;top:1773px;color:var(--red);font-size:18px}
.about-title{left:670px;top:1815px;font-size:42px;font-weight:700;color:var(--navy);line-height:44px}
.about-title .red{color:var(--red)}
.about-copy{left:672px;top:1945px;width:478px;font-size:18px;line-height:31px;color:var(--ink)}

/* reviews */
.remodel{left:0;top:2440px;width:1200px;height:648px;background:linear-gradient(180deg,#2c2c2c,#3b3a38 60%,#2a2927)}
.review-card{left:222px;top:2240px;width:778px;height:428px;background:#fafafc}
.review-title{left:0;top:22px;width:778px;text-align:center;font-size:28px}
.arrow{position:absolute;width:36px;height:36px;border-radius:50%;background:var(--red);color:var(--white);display:flex;align-items:center;justify-content:center;font-size:18px}
.reviewer{left:48px;top:212px;width:170px;text-align:center;font-size:18px;line-height:20px}
.reviewer b{display:block}
.quote-mark{left:218px;top:200px;color:var(--red);font-size:64px;font-weight:700;line-height:60px}
.quote{left:258px;top:212px;width:460px;text-align:center;font-size:17px;font-weight:700;line-height:24px}
.remodel-text{left:0;width:1200px;text-align:center;color:var(--white)}

/* gallery */
.tile{position:absolute;width:349px;height:254px}

/* transformation */
.transform{left:0;top:4055px;width:1200px;height:635px;background:var(--night)}
.tag{position:absolute;top:4573px;height:50px;background:rgba(70,80,84,.85);color:var(--white);font-size:24px;display:flex;align-items:center;justify-content:center}

/* footer */
.footer{left:0;top:4690px;width:1200px;height:505px;background:var(--navy);color:var(--white)}
.foot-logo{left:85px;top:4747px;width:176px;height:176px;border-radius:50%;background:#f7f1f1;display:flex;align-items:center;justify-content:center;flex-direction:column;gap:8px}
.foot-logo span{color:var(--navy);font-size:20px;font-weight:700;letter-spacing:2px}
.foot-head{position:absolute;top:4760px;color:var(--white);font-size:24px}
.foot-links{position:absolute;top:4818px;list-style:none;font-size:18px;color:var(--white)}
.foot-links li{height:41px}
.foot-phone{left:927px;top:4818px;color:var(--red);font-size:30px}
.contact-btn{left:925px;top:4880px;width:178px;height:50px;border:1px solid var(--white);color:var(--white);font-size:19px;text-transform:none}
.social{position:absolute;top:4956px;width:22px;height:22px;border-radius:50%;background:var(--white)}
.info{position:absolute;top:5055px;color:var(--white);font-size:18px;line-height:22px}
.copyright{left:0;top:5155px;width:1200px;text-align:center;font-size:19px;color:var(--white)}
</style>
</head>
<body>

<!-- header -->
<div class="abs brand"><div class="brand-mark"></div><div class="brand-name">BRUSH HARBOR</div></div>
<nav class="nav">
  <a class="home" href="#">HOME</a>
  <a href="#" style="left:680px;top:59px">SERVICES</a>
  <a href="#" style="left:778px;top:59px">ABOUT US</a>
  <a href="#" style="left:878px;top:59px">BLOG</a>
  <a class="cta" href="#">GET FREE ESTIMATE</a>
</nav>

<!-- hero -->
<section class="abs hero">
  <svg class="abs" style="left:0;top:0" width="1200" height="658" viewBox="0 0 1200 658" role="img" aria-label="Mountain harbor village at sunset">
    <defs>
      <linearGradient id="sky" x1="0" y1="0" x2="0" y2="1">
        <stop offset="0" stop-color="#f2a24a"/>
        <stop offset=".45" stop-color="#8a5a3c"/>
        <stop offset=".7" stop-color="#b4633a"/>
        <stop offset="1" stop-color="#6d7d8a"/>
      </linearGradient>
    </defs>
    <path d="M600 0 C540 150 620 330 600 450 C590 560 650 630 680 658 L1200 658 L1200 0 Z" fill="var(--red)"/>
    <path d="M625 0 C565 150 645 330 625 450 C615 560 675 630 705 658 L1200 658 L1200 0 Z" fill="url(#sky)"/>
  </svg>
  <h1 class="abs hero-title">High-Quality<br>Elk Grove Painters</h1>
  <div class="abs hero-sub">Commercial + Residential Sacramento Painters</div>
  <a class="btn btn-red" style="left:48px;top:425px;width:198px;height:50px">Free Estimate</a>
  <a class="btn btn-line-white" style="left:272px;top:425px;width:198px;height:50px">Learn More</a>
</section>

<!-- services -->
<h2 class="section-title" style="top:846px;color:var(--navy);font-weight:700">Extensive <span style="color:var(--red)">Painting</span> Services</h2>
<div class="rule" style="left:553px;top:898px;width:94px"></div>

<article class="card card-navy" style="left:37px">
  <div class="photo" role="img" aria-label="Two-story house exterior" style="background:linear-gradient(180deg,#8fa6c2,#6b6f72 60%,#5a6b48)"></div>
  <h3>Cabinet painting</h3>
  <p>We understand the value of what it means every time someone chooses a painting contractor.</p>
  <a class="btn more more-red">Read more</a>
</article>
<article class="card card-red" style="left:419px">
  <div class="photo" role="img" aria-label="Brush applying orange paint" style="background:linear-gradient(135deg,#7a1c10,#e5582a 50%,#f3a05a)"></div>
  <h3>Fence painting</h3>
  <p style="color:#fbd9dd">We understand the value of what it means every time someone chooses a painting contractor.</p>
  <a class="btn more more-line">Read more</a>
</article>
<article class="card card-navy" style="left:801px">
  <div class="photo" role="img" aria-label="Bright living room with bookshelves" style="background:linear-gradient(180deg,#e8e6e2,#c9c2b8 60%,#6a4a36)"></div>
  <h3>Commercial&nbsp; painting</h3>
  <p>We understand the value of what it means every time someone chooses a painting contractor.</p>
  <a class="btn more more-red">Read more</a>
</article>

<a class="btn btn-red" style="left:341px;top:1536px;width:240px;height:60px">Free Estimate</a>
<a class="btn btn-line-red" style="left:597px;top:1536px;width:280px;height:60px">View&nbsp; All Service</a>

<!-- about -->
<div class="abs about-bg"></div>
<div class="photo framed" role="img" aria-label="Kitchen with white cabinets" style="left:222px;top:1770px;width:400px;height:270px;background:linear-gradient(160deg,#e4e1dc,#9b948a 55%,#5b3a2a)"></div>
<div class="photo framed" role="img" aria-label="Renovated white kitchen" style="left:40px;top:1892px;width:368px;height:250px;background:linear-gradient(180deg,#eceae6,#cfd0cf 60%,#8d8c88)"></div>
<div class="abs kicker">ABOUT US</div>
<h2 class="abs about-title">Painting<br><span class="red">Guaranteed</span> to Last</h2>
<div class="rule" style="left:672px;top:1920px;width:98px"></div>
<p class="abs about-copy">We understand the value of what it means every time someone chooses a painting contractor. That’s why we use only the highest-quality materials and work hard to ensure you’re happy once the project is complete. We provide our painting and epoxy services to everyone in and around Sacramento County</p>

<!-- remodel band with reviews -->
<section class="abs remodel" role="img" aria-label="Dim living room with sofa and shelves"></section>
<div class="abs review-card">
  <h2 class="abs review-title">Reviews</h2>
  <div class="abs" style="left:343px;top:72px;width:20px;height:4px;background:var(--ink)"></div>
  <div class="abs" style="left:369px;top:72px;width:20px;height:4px;background:var(--red)"></div>
  <div class="abs" style="left:395px;top:72px;width:20px;height:4px;background:var(--red)"></div>
  <div class="abs" style="left:421px;top:72px;width:20px;height:4px;background:var(--red)"></div>
  <div class="photo" role="img" aria-label="Customer portrait" style="left:83px;top:90px;width:100px;height:100px;border-radius:50%;background:linear-gradient(180deg,#cfd6de,#4b6a8c)"></div>
  <div class="arrow" style="left:12px;top:207px">&lt;</div>
  <div class="abs reviewer"><b>DALE OSTRANDER</b>Elk Grove</div>
  <div class="abs" style="left:238px;top:123px;width:1px;height:230px;background:#555"></div>
  <div class="abs quote-mark">,,</div>
  <p class="abs quote">"The quality of their final product exceeded all our expectations."</p>
  <div class="arrow" style="left:720px;top:207px">&gt;</div>
</div>
<div class="abs remodel-text" style="top:2756px;font-size:19px">HOME REMODEL</div>
<div class="abs remodel-text" style="top:2796px;font-size:48px;line-height:54px">Your <span style="color:var(--red)">Dream Home</span><br>Awaits</div>

<!-- gallery -->
<h2 class="section-title" style="top:3160px;font-weight:400">Gallery</h2>
<div class="rule" style="left:563px;top:3206px;width:80px"></div>
<div class="tile" role="img" aria-label="House facade with dormers" style="left:42px;top:3277px;background:linear-gradient(180deg,#3c3f44,#dcdcd6 50%,#4a5a3c)"></div>
<div class="tile" role="img" aria-label="Suburban home with garage" style="left:422px;top:3277px;background:linear-gradient(180deg,#4d79b8,#a9a49a 50%,#8c8b86)"></div>
<div class="tile" role="img" aria-label="Kitchen with steel appliances" style="left:802px;top:3277px;background:linear-gradient(160deg,#e9e5df,#4c4644 60%,#6a4a36)"></div>
<div class="tile" role="img" aria-label="Room with shelves and leather chair" style="left:42px;top:3561px;background:linear-gradient(180deg,#ecebe7,#c8bfae 60%,#4b3326)"></div>
<div class="tile" role="img" aria-label="White kitchen with window" style="left:422px;top:3561px;background:linear-gradient(180deg,#d7d7d6,#f0f0ee 55%,#8f9399)"></div>
<div class="tile" role="img" aria-label="Red car front detail" style="left:802px;top:3561px;background:linear-gradient(180deg,#2a2a2a,#c81824 40%,#6e6e6e)"></div>
<a class="btn btn-red" style="left:450px;top:3870px;width:305px;height:60px">View Full Gallery</a>

<!-- transformation -->
<section class="abs transform"></section>
<h2 class="section-title" style="top:4097px;color:var(--white);font-weight:400">See The Transformation</h2>
<div class="photo" role="img" aria-label="Shed before painting" style="left:199px;top:4183px;width:416px;height:440px;background:linear-gradient(180deg,#9a9a9a,#d8d8d8 50%,#6a6a6a)"></div>
<div class="photo" role="img" aria-label="Shed after painting" style="left:615px;top:4183px;width:372px;height:440px;background:linear-gradient(180deg,#3f6fb5,#c9a47a 45%,#7a5a3c)"></div>
<div class="tag" style="left:199px;width:149px">Before</div>
<div class="tag" style="left:858px;width:129px">After</div>

<!-- footer -->
<footer class="abs footer"></footer>
<div class="abs foot-logo"><div style="width:22px;height:22px;border-radius:50%;background:var(--red)"></div><span>BRUSH HARBOR</span></div>

<div class="foot-head" style="left:397px">Contact Links</div>
<div class="rule" style="left:397px;top:4798px;width:98px"></div>
<ul class="foot-links" style="left:399px"><li>Home</li><li>Services</li><li>Gallery</li><li>Blog</li></ul>

<div class="foot-head" style="left:634px">Services</div>
<div class="rule" style="left:634px;top:4798px;width:98px"></div>
<ul class="foot-links" style="left:636px"><li>Cabinet Painting</li><li>Fence&nbsp; Painting</li><li>Interior Painting</li><li>Commercial Painting</li></ul>

<div class="foot-head" style="left:916px;top:4763px">Get Free Estimate</div>
<div class="rule" style="left:922px;top:4800px;width:98px"></div>
<div class="abs foot-phone">925 555 0148</div>
<a class="btn contact-btn">Contact&nbsp; Us</a>
<div class="social" style="left:930px"></div>
<div class="social" style="left:970px"></div>
<div class="social" style="left:1005px"></div>
<div class="social" style="left:1040px"></div>

<svg class="abs" style="left:152px;top:5048px" width="20" height="30" viewBox="0 0 20 30"><path d="M10 0a10 10 0 0 1 10 10c0 8-10 20-10 20S0 18 0 10A10 10 0 0 1 10 0z" fill="var(--red)"/><circle cx="10" cy="10" r="4" fill="var(--navy)"/></svg>
<div class="info" style="left:196px">18 B, Lantern Road<br>Oak Hollow</div>
<svg class="abs" style="left:452px;top:5054px" width="24" height="24" viewBox="0 0 24 24"><path d="M6 2l4 4-2 3c1 3 4 6 7 7l3-2 4 4-3 4C10 22 2 14 2 5z" fill="var(--red)"/></svg>
<div class="info" style="left:498px;top:5057px">Phone: 555 201 7734</div>
<svg class="abs" style="left:752px;top:5058px" width="26" height="18" viewBox="0 0 26 18"><rect width="26" height="18" fill="var(--red)"/><path d="M0 0l13 10L26 0" fill="none" stroke="var(--navy)" stroke-width="2"/></svg>
<div class="info" style="left:798px;top:5057px">hello@brushharbor.example</div>
<div class="abs" style="left:0;top:5128px;width:1200px;height:1px;background:rgba(255,255,255,.5)"></div>
<div class="abs copyright">© Copyright Reserved by Brush Harbor</div>

</body>
</html>
```